Korvune Site

We are looking for someone to help build a information site of our product Korvune for Sickle Cell Disease

Industry/Entity Type

Patent Educational Site

Coding

Coded - Design and coding required

Number of Pages Required

5+ page

Font styles to use
Sans Serif

Colors
EB3D1F
EC4F4E
F09395
F8D3D4
FCEDEE

```html
<!DOCTYPE html>
<html lang="en">
<head>
<meta charset="utf-8">
<title>Korvune – Medical Food for Sickle Cell Disease</title>
<link href="https://fonts.googleapis.com/css2?family=Roboto:wght@400;500;700&family=Signika:wght@400;600;700&family=Teko:wght@500;600&display=swap" rel="stylesheet">
<style>
:root{
  --red:#eb3d1f;
  --coral:#ec4f4e;
  --rose:#f09395;
  --blush:#f8d3d4;
  --mist:#fcedee;
  --crimson:#b2282d;
  --navy:#1b1f5c;
  --ink:#3a3a3a;
  --charcoal:#232021;
  --panel:#efefef;
}
*{margin:0;padding:0;box-sizing:border-box}
html,body{width:1200px;height:2858px;overflow:hidden;background:#fff}
body{position:relative;font-family:'Roboto',sans-serif;color:var(--ink)}
.abs{position:absolute}

/* header */
.site-header{position:absolute;left:0;top:0;width:1200px;height:80px;background:#fff;border-top:3px solid var(--red);z-index:3}
.brand{position:absolute;left:42px;top:12px;display:flex;align-items:center;gap:8px;font-family:'Signika',sans-serif;font-weight:600;font-size:34px;color:var(--crimson);line-height:1}
.brand-dot{width:12px;height:12px;border-radius:50%;background:var(--crimson)}
.main-nav{position:absolute;left:471px;top:30px;display:flex;gap:22px;font-size:12.5px;font-weight:700;color:var(--navy);letter-spacing:.1px}
.btn-support{position:absolute;left:1010px;top:16px;width:145px;height:41px;border-radius:21px;background:var(--crimson);color:#fff;font-size:12.5px;font-weight:700;display:flex;align-items:center;justify-content:center}

/* hero */
.hero{position:absolute;left:0;top:80px;width:1200px;height:641px;overflow:hidden}
.hero-photo{position:absolute;inset:0;background:linear-gradient(100deg,#e8ecef 35%,#c9d9e8 55%,#8fb4d8 70%,#c8a98a 90%,#e9eef2)}
.hero svg{position:absolute;left:0;top:0}
.hero-title{position:absolute;left:42px;top:186px;font-family:'Signika',sans-serif;font-weight:700;font-size:52px;color:var(--navy);line-height:1}
.hero-sub{position:absolute;left:98px;top:245px;font-family:'Signika',sans-serif;font-weight:600;font-size:17px;color:var(--navy);letter-spacing:.2px}
.hero-disease{position:absolute;left:41px;top:265px;font-family:'Signika',sans-serif;font-weight:600;font-size:50px;color:var(--red);line-height:1.1}
.hero-note{position:absolute;left:116px;top:317px;font-family:'Signika',sans-serif;font-size:19px;color:var(--navy)}
.btn-pill{position:absolute;border-radius:24px;background:var(--crimson);color:#fff;font-weight:700;display:flex;align-items:center;justify-content:center}
.hero .btn-pill{left:160px;top:364px;width:150px;height:44px;font-family:'Signika',sans-serif;font-size:15px;font-weight:600}
.hero-dots{position:absolute;left:532px;top:341px;display:flex;gap:6px}
.hero-dots i{width:20px;height:20px;border-radius:50%;display:block}

/* welcome */
.welcome-kicker{left:46px;top:770px;font-family:'Signika',sans-serif;font-weight:600;font-size:17px;color:var(--navy)}
.welcome-title{left:41px;top:789px;font-family:'Signika',sans-serif;font-weight:700;font-size:52px;color:var(--red);line-height:1;display:flex;align-items:baseline;gap:14px}
.welcome-title small{font-family:'Signika',sans-serif;font-weight:400;font-size:30px;color:var(--navy)}
.welcome-copy{left:41px;top:856px;width:621px;font-size:13.2px;line-height:19.5px;text-align:justify}
.col-head{top:975px;font-family:'Signika',sans-serif;font-weight:600;font-size:18px;color:var(--navy)}
.col-head::after{content:"";display:block;width:62px;height:3px;background:var(--red);margin-top:6px}
.bullets{top:1020px;list-style:none;font-size:13.2px;line-height:21px}
.bullets li{padding-left:15px;position:relative}
.bullets li::before{content:"";position:absolute;left:0;top:6px;width:9px;height:9px;border-radius:50%;background:var(--navy)}
.welcome .btn-pill{left:42px;top:1111px;width:135px;height:42px;font-size:12.5px}
.welcome-photo{left:705px;top:758px;width:452px;height:430px;border-radius:70% 30% 40% 60% / 40% 55% 45% 60%;background:linear-gradient(135deg,#d9c6b6,#e8dcd0 45%,#c7c3c7 70%,#ede6df)}

/* band */
.band{position:absolute;left:0;top:1207px;width:1200px;height:227px}
.band-text{position:absolute;left:0;top:1287px;width:1200px;text-align:center;color:#fff;font-size:30px;line-height:36px}

/* cards */
.topic-card{position:absolute;top:1473px;width:261px;height:297px;border-radius:18px;overflow:hidden}
.topic-card .photo{position:absolute;inset:0}
.topic-card svg{position:absolute;left:0;bottom:0}
.topic-card .label{position:absolute;left:0;bottom:14px;width:100%;padding:0 40px;text-align:center;font-size:15px;font-weight:500;color:var(--ink);line-height:18px}
.pager{position:absolute;left:566px;top:1802px;display:flex;gap:4px}
.pager i{width:12px;height:12px;border-radius:50%;border:1px solid var(--rose);display:block}
.pager i:first-child{background:var(--red);border-color:var(--red)}

/* info */
.info-panel{left:42px;top:1866px;width:1115px;height:349px;border-radius:24px;background:var(--panel)}
.info-copy{left:427px;top:1935px;width:691px;font-size:13.2px;line-height:19.45px;text-align:justify}

/* footer */
.site-footer{position:absolute;left:0;top:2290px;width:1200px;height:568px}
.footer-brand{position:absolute;left:508px;top:2312px;display:flex;align-items:center;gap:8px;font-family:'Signika',sans-serif;font-weight:600;font-size:36px;color:var(--crimson)}
.footer-brand i{width:12px;height:12px;border-radius:50%;background:var(--crimson);display:block}
.cta-title{left:0;top:2440px;width:1200px;text-align:center;font-family:'Teko',sans-serif;font-weight:600;font-size:58px;color:#fff;line-height:1;letter-spacing:.5px}
.cta-sub{left:0;top:2490px;width:1200px;text-align:center;font-size:14px;color:#eee}
.signup{left:347px;top:2535px;width:473px;height:39px;display:flex}
.signup .field{flex:1;border:1px solid #888;border-right:none;display:flex;align-items:center;gap:8px;padding-left:14px;color:#ddd;font-size:10.5px}
.signup .go{width:107px;background:var(--red);color:#fff;font-weight:700;font-size:14px;display:flex;align-items:center;justify-content:center}
.footer-text{left:200px;top:2602px;width:800px;text-align:center;font-size:11.5px;line-height:20px;color:#eee}
.social{position:absolute;top:2664px;width:34px;height:34px;border-radius:50%;border:1.5px solid #ddd}
.contact{top:2736px;display:flex;align-items:center;gap:6px;font-size:11px;color:#fff}
.copyright{position:absolute;left:0;top:2797px;width:1200px;height:61px;background:var(--crimson);color:#fff;font-size:13px;display:flex;align-items:center;justify-content:center}
</style>
</head>
<body>

<header class="site-header">
  <div class="brand">Korvune <span class="brand-dot"></span></div>
  <nav class="main-nav">
    <span>WHAT IS KORVUNE</span><span>ABOUT SCD</span><span>HOW KORVUNE WORKS</span><span>INSURANCE COVERAGE</span>
  </nav>
  <div class="btn-support">PATIENT SUPPORT</div>
</header>

<section class="hero">
  <div class="hero-photo" role="img" aria-label="Nurse smiling with an older patient seated in a wheelchair in a clinic hallway"></div>
  <svg width="1200" height="641" viewBox="0 0 1200 641" aria-hidden="true">
    <defs>
      <linearGradient id="heroFade" x1="0" y1="0" x2="1" y2="1">
        <stop offset="0" stop-color="#ffffff"/>
        <stop offset=".6" stop-color="#fbf0f0"/>
        <stop offset="1" stop-color="#f6d9da"/>
      </linearGradient>
    </defs>
    <polygon points="0,0 510,0 682,345 410,641 0,641" fill="url(#heroFade)"/>
  </svg>
  <div class="hero-title">A MEDICAL FOOD</div>
  <div class="hero-sub">FOR THE DIETARY MANAGEMENT OF</div>
  <div class="hero-disease">Sickle Cell Disease</div>
  <div class="hero-note">in Pediatric and Adult Patients</div>
  <div class="btn-pill">GET IN TOUCH</div>
  <div class="hero-dots">
    <i style="background:var(--red)"></i><i style="background:var(--coral)"></i><i style="background:var(--rose)"></i><i style="background:var(--blush)"></i><i style="background:var(--mist)"></i>
  </div>
</section>

<section class="welcome">
  <div class="abs welcome-kicker">WELCOME TO</div>
  <div class="abs welcome-title">KORVUNE <small>by velmora</small></div>
  <p class="abs welcome-copy">Korvune is a medical food emulsification formulated to provide a high concentration of triglycerides of certain fatty acids, to replenish the those consumed by the hemoglobin (HbS) characteristic of SCD.&nbsp; In clinical trials conducted under a US Investigational New Drug Application, a similar consumption of these fatty acids provided data indicating an impact on the cascade leading to vaso-occlusive events.&nbsp; Korvune® was formulated to provide the same fatty acids used in these trials in a good tasting oral formulation highly that bioavailable.</p>
  <h3 class="abs col-head" style="left:41px">Features and Benefits</h3>
  <ul class="abs bullets" style="left:41px;width:300px">
    <li>Formulated for Enhanced Absorption1</li>
    <li>Manage VOC Events2</li>
    <li>Lower C-reactive Protein (Inflammation) Levels3</li>
  </ul>
  <h3 class="abs col-head" style="left:360px">Key ingredients</h3>
  <ul class="abs bullets" style="left:360px;width:302px">
    <li>Enriched docosahexaenoic acid triglycerides, egg yolk (lecitin), and d-limonene</li>
    <li>Contains egg and fish (anchovy, sardine)</li>
  </ul>
  <div class="btn-pill">READ MORE ›</div>
  <div class="abs welcome-photo" role="img" aria-label="Doctor with a tablet talking with a young girl sitting on her mother's lap"></div>
</section>

<svg class="band" viewBox="0 0 1200 227" aria-hidden="true">
  <path d="M0 0 Q600 80 1200 0 V227 Q600 170 0 227 Z" fill="var(--crimson)"/>
</svg>
<p class="band-text">Ask your doctor or dietitian for more information about Korvune®.<br>Use under medical supervision.</p>

<section class="topics">
  <div class="topic-card" style="left:42px">
    <div class="photo" role="img" aria-label="Smiling young girl eating a meal with her mother" style="background:linear-gradient(160deg,#e9e4de,#c79a7a 45%,#7a4a3a 75%,#d9d2cc)"></div>
    <svg width="261" height="110" viewBox="0 0 261 110" aria-hidden="true"><path d="M0 52 H180 Q205 52 220 32 Q235 14 245 40 L261 72 V110 H0 Z" fill="#f4b2b3"/></svg>
    <div class="label">What is Korvune</div>
  </div>
  <div class="topic-card" style="left:327px">
    <div class="photo" role="img" aria-label="Red blood cells including sickle-shaped cells" style="background:radial-gradient(circle at 50% 45%,#b3231f,#5a0d0d 55%,#2a0606)"></div>
    <svg width="261" height="110" viewBox="0 0 261 110" aria-hidden="true"><path d="M0 52 H180 Q205 52 220 32 Q235 14 245 40 L261 72 V110 H0 Z" fill="#f4b2b3"/></svg>
    <div class="label">About Sickle Cell Disease</div>
  </div>
  <div class="topic-card" style="left:612px">
    <div class="photo" role="img" aria-label="Hands sheltering a family figure, symbolising insurance coverage" style="background:linear-gradient(170deg,#8fb6d6,#bcd6ea 50%,#e9d8cc)"></div>
    <svg width="261" height="110" viewBox="0 0 261 110" aria-hidden="true"><path d="M0 52 H180 Q205 52 220 32 Q235 14 245 40 L261 72 V110 H0 Z" fill="#f4b2b3"/></svg>
    <div class="label">Insurance Coverage</div>
  </div>
  <div class="topic-card" style="left:895px">
    <div class="photo" role="img" aria-label="Nurse supporting an older woman" style="background:linear-gradient(160deg,#d8d2c8,#9aa9a0 40%,#7fa3cf 70%,#e4ded6)"></div>
    <svg width="261" height="110" viewBox="0 0 261 110" aria-hidden="true"><path d="M0 52 H180 Q205 52 220 32 Q235 14 245 40 L261 72 V110 H0 Z" fill="#f4b2b3"/></svg>
    <div class="label">Patient Support</div>
  </div>
  <div class="pager"><i></i><i></i><i></i><i></i><i></i></div>
</section>

<section class="info">
  <div class="abs info-panel"></div>
  <svg class="abs" style="left:76px;top:1889px" width="312" height="298" viewBox="0 0 312 298" role="img" aria-label="Close view of red blood cells and sickle cells">
    <defs>
      <radialGradient id="cellGlow" cx=".45" cy=".45" r=".7">
        <stop offset="0" stop-color="#8e1a18"/><stop offset=".6" stop-color="#4a0909"/><stop offset="1" stop-color="#220404"/>
      </radialGradient>
    </defs>
    <path d="M40 30 Q90 -5 150 30 L285 140 Q320 175 280 205 Q200 270 120 292 Q60 305 35 250 Q0 150 10 80 Q15 45 40 30 Z" fill="url(#cellGlow)" stroke="#f8d3d4" stroke-width="4"/>
  </svg>
  <p class="abs info-copy">The Congress of the United States enacted Orphan Drug Act (21 U.S.C. 360ee(b)(3)) which stated in section 5(b)(3) that a new category of treatment for a small number of diseases, one of which was sickle cell disease, is now allowed.&nbsp; These treatment modalities require clinical and scientific evidence before they can enter commerce, but the Act also allows such products to become available through an abbreviated process, avoiding the high cost of a New Drug Application.&nbsp; The term medical food, as defined in section 5(b) of the Orphan Drug Act is "a food which is formulated to be consumed or administered enterally (by mouth) under the supervision of a physician and which is intended for the specific dietary management of a disease or condition for which distinctive nutritional requirements, based on recognized scientific principles, are established by medical evaluation." Velmora and Company, the creator of Korvune®, began research on sickle cell disease in 2011.&nbsp; From over a decade of work, Korvune® was created and will soon become available globally in 2023. Korvune® is a Medical Food that is intended to restore the balance in the cellular membrane of people with sickle cell disease and may have a significant beneficial effect.</p>
</section>

<svg class="site-footer" viewBox="0 0 1200 568" aria-hidden="true">
  <path d="M0 67 Q600 -20 1200 67 V568 H0 Z" fill="var(--charcoal)"/>
  <circle cx="590" cy="15" r="119" fill="#fff"/>
</svg>
<div class="footer-brand">Korvune <i></i></div>
<div class="abs cta-title">LET'S GET MOVING</div>
<div class="abs cta-sub">SIGN UP FOR UPDATES</div>
<div class="abs signup">
  <div class="field">
    <svg width="14" height="11" viewBox="0 0 14 11" aria-hidden="true"><rect x=".75" y=".75" width="12.5" height="9.5" fill="none" stroke="#ddd" stroke-width="1.2"/><path d="M1 1 L7 6 L13 1" fill="none" stroke="#ddd" stroke-width="1.2"/></svg>
    Enter Your Email Id
  </div>
  <div class="go">SUBSCRIBE</div>
</div>
<p class="abs footer-text">Lorem Ipsum is simply dummy text of the printing and typesetting industry. Lorem Ipsum has been the industry's standard dummy text ever<br>containing Lorem Ipsum passages, and more recently with desktop publishing software like Quillset Layout including versions</p>
<span class="social" style="left:493px"></span>
<span class="social" style="left:537px"></span>
<span class="social" style="left:582px"></span>
<span class="social" style="left:626px"></span>
<div class="abs contact" style="left:352px">
  <svg width="8" height="11" viewBox="0 0 8 11" aria-hidden="true"><path d="M4 0 A4 4 0 0 1 8 4 C8 7 4 11 4 11 C4 11 0 7 0 4 A4 4 0 0 1 4 0 Z" fill="#fff"/><circle cx="4" cy="4" r="1.5" fill="#232021"/></svg>
  Lorem Ipsum is simply dummy text.
</div>
<div class="abs contact" style="left:584px">
  <svg width="11" height="8" viewBox="0 0 11 8" aria-hidden="true"><rect width="11" height="8" fill="#fff"/><path d="M0 0 L5.5 4.5 L11 0" fill="none" stroke="#232021"/></svg>
  info@Korvune.com
</div>
<div class="abs contact" style="left:733px">
  <svg width="10" height="10" viewBox="0 0 10 10" aria-hidden="true"><path d="M2 0 L4 2.5 L3 4 Q4.5 6 6 7 L7.5 6 L10 8 L8.5 10 Q3 9 0 1.5 Z" fill="#fff"/></svg>
  123-456-7890
</div>
<div class="copyright">Copyright 2023 Korvune.com. All Right Reserved.</div>

</body>
</html>
```